BRASKET LAND SERVICES BILLBOARD DESIGN

I NEED A BILLBOARD FOR MY BUSINESS. WE ARE A LAND CLEARING COMPANY AND I WOULD LIKE TO ADD A PICTURE OF MY TRACK LOADER TO THE SIGN. OPEN TO COLORS. I WOULD ALSO LIKE TO HAVE MY PHONE NUMBER 555-284-6170, WEBSITE WWW.BRASKETLANDSERVICES.EXAMPLE, AND EMAIL ON THE SIGN (CONTACT@BRASKETLANDSERVICES.EXAMPLE). DESIGNERS CAN HAVE THE FREEDOM TO DO WHATEVER STYLE THEY WANT AND TO USE ANY COLORS THEY WANT.

Target Market(s)

ANYONE WITH PROPERTY

Requirements
Must have
• PICTURE OF TRACK LOADER, WEBSITE, PHONE NUMBER, EMAIL
Nice to have
• OPEN TO ANYTHING
Should not have
• OPEN TO ANYTHING

```html
<!DOCTYPE html>
<html lang="en">
<head>
<meta charset="utf-8">
<title>Brasket Land Services Billboard</title>
<link href="https://fonts.googleapis.com/css2?family=Montserrat:ital,wght@1,800;1,900&display=swap" rel="stylesheet">
<style>
  :root {
    --orange: #f26a21;
    --black: #141414;
    --panel: #1c1c1c;
    --white: #ffffff;
    --page: #e9eaec;
    --grass: #8e8a4a;
    --forest: #3f4a2a;
  }
  html, body {
    margin: 0;
    width: 1200px;
    height: 1188px;
    overflow: hidden;
    background: var(--page);
  }
  .billboard {
    position: absolute;
    left: 0;
    top: 418px;
    width: 1200px;
    height: 352px;
    overflow: hidden;
    font-family: "Montserrat", sans-serif;
    font-style: italic;
  }
  .billboard-shapes {
    position: absolute;
    inset: 0;
  }
  .copy {
    position: absolute;
    margin: 0;
    line-height: 1;
    white-space: nowrap;
    font-weight: 900;
  }
  .brand-name { left: 72px; top: 40px; font-size: 62px; color: var(--orange); letter-spacing: 1px; }
  .brand-tagline { left: 68px; top: 110px; font-size: 45px; color: var(--white); }
  .call-now { left: 72px; top: 186px; font-size: 29px; color: var(--orange); font-weight: 800; }
  .phone { left: 66px; top: 224px; font-size: 53px; color: var(--white); letter-spacing: 1px; }
  .website { left: 70px; top: 300px; font-size: 19px; color: var(--black); }
  .email { left: 64px; top: 322px; font-size: 19px; color: var(--black); }
</style>
</head>
<body>
  <section class="billboard">
    <svg class="billboard-shapes" width="1200" height="352" viewBox="0 0 1200 352">
      <defs>
        <linearGradient id="loader-photo-tone" x1="0" y1="0" x2="0" y2="1">
          <stop offset="0" stop-color="var(--forest)"/>
          <stop offset="0.55" stop-color="#5e6236"/>
          <stop offset="1" stop-color="var(--grass)"/>
        </linearGradient>
      </defs>
      <rect class="backdrop" width="1200" height="352" fill="var(--black)"/>
      <polygon class="top-band" points="0,0 905,0 890,16 0,16" fill="var(--orange)"/>
      <polygon class="top-band-rule" points="0,16 890,16 884,22 0,22" fill="var(--white)"/>
      <polygon class="corner-stripe" points="905,0 1010,0 1200,40 1200,58" fill="var(--white)"/>
      <polygon class="left-panel" points="0,22 630,22 650,42 650,288 0,288" fill="var(--panel)"/>
      <polygon class="photo-frame" points="640,16 1130,16 1160,36 1200,36 1200,306 692,306 640,256" fill="var(--white)"/>
      <polygon class="photo-area" role="img" aria-label="Photo of an orange tracked loader with a forestry mulcher attachment in a cleared wooded lot" points="658,30 1124,30 1154,50 1188,50 1188,294 698,294 658,250" fill="url(#loader-photo-tone)"/>
      <polygon class="contact-band" points="0,290 660,290 712,352 0,352" fill="var(--white)"/>
      <polygon class="contact-band-edge" points="660,290 700,290 752,352 712,352" fill="var(--black)"/>
      <polygon class="corner-accent" points="935,352 955,328 1200,328 1200,352" fill="var(--orange)"/>
    </svg>
    <h1 class="copy brand-name">BRASKET</h1>
    <p class="copy brand-tagline">LAND SERVICES</p>
    <p class="copy call-now">CALL NOW!</p>
    <p class="copy phone">555-284-6170</p>
    <p class="copy website">WWW.BRASKETLANDSERVICES.EXAMPLE</p>
    <p class="copy email">CONTACT@BRASKETLANDSERVICES.EXAMPLE</p>
  </section>
</body>
</html>
```